Letterhead Design

I would like 2 different letterheads. One with each logo I have attached. Business info:
Larkfield Medical Billing, LLC
3870 N Cedar
Ossing, KS 66492
(866) 555-0143

```html
<!DOCTYPE html>
<html lang="en">
<head>
<meta charset="utf-8">
<title>Larkfield Medical Billing – Letterhead</title>
<link rel="stylesheet" href="https://fonts.googleapis.com/css2?family=Cormorant+Garamond:wght@500&family=Fira+Sans+Extra+Condensed:wght@400&display=swap">
<style>
  :root {
    --backdrop: #e9e6e1;
    --paper: #ffffff;
    --gold: #b39a64;
    --gold-light: #ecd9a6;
    --gold-dark: #b29a68;
    --red: #c40d0d;
    --ink: #222222;
  }
  * { margin: 0; padding: 0; box-sizing: border-box; }
  html, body {
    width: 941px;
    height: 1200px;
    overflow: hidden;
    background: var(--backdrop);
  }
  .letterhead {
    position: absolute;
    left: 50px;
    top: 66px;
    width: 840px;
    height: 1086px;
    background: var(--paper);
    box-shadow: 0 2px 10px rgba(0, 0, 0, 0.25);
    overflow: hidden;
  }
  .brand {
    position: absolute;
    left: 30px;
    top: 12px;
    width: 180px;
    text-align: center;
    font-family: "Cormorant Garamond", Georgia, serif;
    font-weight: 500;
    color: var(--gold);
  }
  .brand-mark {
    display: block;
    width: 64px;
    height: 64px;
    margin: 8px auto 16px;
    border-radius: 50%;
    background: var(--gold);
  }
  .brand-name {
    font-size: 22px;
    line-height: 1.15;
    letter-spacing: 1px;
  }
  .contact {
    position: absolute;
    left: 22px;
    top: 1040px;
    display: flex;
    gap: 26px;
    font-family: "Fira Sans Extra Condensed", "Arial Narrow", sans-serif;
    font-size: 18px;
    color: var(--ink);
  }
  .contact-item {
    display: flex;
    align-items: center;
    gap: 5px;
  }
  .contact-item svg { width: 14px; height: 16px; fill: var(--ink); }
  .footer-bands {
    position: absolute;
    left: 0;
    bottom: 0;
    width: 840px;
    height: 42px;
  }
</style>
</head>
<body>
  <main class="letterhead">
    <header class="brand">
      <span class="brand-mark"></span>
      <div class="brand-name">Larkfield<br>Medical Billing</div>
    </header>

    <footer>
      <div class="contact">
        <span class="contact-item">
          <svg viewBox="0 0 14 16" aria-hidden="true"><path d="M4 1c1 0 1.5 2.5 1.5 3.5S4 5.5 4 6.5s1.5 4 3 4.5c1 .3 1.5-1.2 2.5-1s2.5 1.8 2.5 2.8S10 15 8.5 15C5 15 1.5 9.5 1.5 5.5 1.5 3 3 1 4 1z"/></svg>
          866-555-0143
        </span>
        <span class="contact-item">
          <svg viewBox="0 0 14 16" aria-hidden="true"><path d="M7 0a5.5 5.5 0 0 0-5.5 5.5C1.5 10 7 16 7 16s5.5-6 5.5-10.5A5.5 5.5 0 0 0 7 0zm0 8a2.5 2.5 0 1 1 0-5 2.5 2.5 0 0 1 0 5z"/></svg>
          3870 N Cedar Ossing, KS 66492
        </span>
      </div>
      <svg class="footer-bands" viewBox="0 0 840 42" aria-hidden="true">
        <defs>
          <linearGradient id="goldBand" x1="0" y1="0" x2="1" y2="0">
            <stop offset="0" stop-color="var(--gold-dark)"/>
            <stop offset="1" stop-color="var(--gold-light)"/>
          </linearGradient>
        </defs>
        <polygon points="0,23 415,23 395,42 0,42" fill="var(--red)"/>
        <polygon points="440,0 840,0 840,42 396,42" fill="url(#goldBand)"/>
      </svg>
    </footer>
  </main>
</body>
</html>
```